Private Chef booking platform landing page design

I need an amazing design for a landing page for my upcoming private chef booking platform Dinvora. You can view my current page here: www.dinvora.co.uk/mainindex.php. The design on this page is wrong right now. This platform is in Beta and the main purpose is to sign up chefs. Similar to what Ridelix.com is doing with their website -> become a driver. In my case we should have a button that says "become a chef", state the benefits of becoming a chef such as earning extra money, managing your time and bookings, increasing your client base and be creative with your food menus at the same time. Also, somewhere on the website it needs to say that we are currently in Beta mode and sign up to help us grow. In terms of visuals, I want the design to be sleek and clean and also adaptable to mobile devices as I am using html5. You can also re-design the current logo and choose any colours you think would be suitable for such a concept. Similar concept websites: platewander.com and cookvey.com
Updates

Target Market(s)

upper middle class

Industry/Entity Type

Chef

Number of Pages Required

1 page

Font styles to use
Sans Serif

Requirements
Must have
• see brief and check platewander.com and cookvey.com for inspiration and also ridelix.com
Nice to have
• see brief
Should not have
• bad visuals

```html
<!DOCTYPE html>
<html lang="en">
<head>
<meta charset="utf-8">
<title>Dinvora — Chef Made Meals In Your Home</title>
<link rel="stylesheet" href="https://fonts.googleapis.com/css2?family=Montserrat:wght@400;600;700&family=Oswald:wght@300;400&family=Playfair+Display:ital@1&display=swap">
<style>
  :root {
    --ink: #111111;
    --header: #0d0d0d;
    --white: #ffffff;
    --brand-yellow: #e9c21b;
    --teal: #7fd3c8;
    --teal-deep: #1d3b3a;
    --hero-a: #6a5a8c;
    --hero-b: #3d3354;
    --hero-c: #2a2238;
    --line: rgba(255,255,255,0.55);
  }
  * { box-sizing: border-box; margin: 0; padding: 0; }
  html, body { width: 1200px; height: 756px; overflow: hidden; background: var(--ink); }
  .page { position: relative; width: 1200px; height: 756px; font-family: "Montserrat", sans-serif; color: var(--white); }

  .site-header {
    position: absolute; top: 0; left: 0; right: 0; height: 84px;
    background: var(--header);
    display: flex; align-items: center; padding: 0 44px;
  }
  .brand { display: flex; align-items: flex-start; gap: 6px; border: 2px solid var(--brand-yellow); padding: 9px 14px; }
  .brand-name { font-weight: 700; font-size: 22px; letter-spacing: 1px; color: var(--brand-yellow); }
  .brand-tag { font-size: 9px; font-weight: 700; margin-top: -2px; margin-right: -50px; color: var(--white); }
  .main-nav { display: flex; align-items: center; gap: 22px; margin-left: 84px; font-size: 11px; font-weight: 700; letter-spacing: .5px; }
  .main-nav .active { color: var(--brand-yellow); border-left: 5px solid var(--brand-yellow); padding-left: 10px; }
  .account-links { margin-left: auto; font-size: 11px; font-weight: 600; letter-spacing: .5px; }
  .account-links span { margin: 0 8px; }

  .hero {
    position: absolute; top: 84px; left: 0; right: 0; bottom: 0;
    background:
      radial-gradient(ellipse at 25% 30%, rgba(190,150,90,.35), transparent 45%),
      radial-gradient(ellipse at 80% 25%, rgba(170,130,80,.3), transparent 40%),
      linear-gradient(160deg, var(--hero-a), var(--hero-b) 55%, var(--hero-c));
  }
  .hero-content { position: absolute; top: 0; left: 0; right: 0; bottom: 0; text-align: center; }
  .hero-title {
    position: absolute; top: 210px; left: 0; right: 0;
    font-family: "Oswald", sans-serif; font-weight: 300; font-size: 50px; letter-spacing: 1px;
  }
  .cta-chef {
    position: absolute; top: 314px; left: 50%; transform: translateX(-50%);
    background: var(--teal); color: var(--teal-deep);
    padding: 9px 24px 8px; outline: 2px solid var(--teal); outline-offset: 3px;
  }
  .cta-chef strong { display: block; font-family: "Oswald", sans-serif; font-weight: 400; font-size: 26px; letter-spacing: .5px; }
  .cta-chef em { display: block; font-family: "Playfair Display", serif; font-size: 15px; border-top: 1px solid var(--teal-deep); padding-top: 2px; }
  .secondary-actions { position: absolute; top: 418px; left: 0; right: 0; display: flex; justify-content: center; gap: 16px; }
  .btn { font-family: "Oswald", sans-serif; font-size: 24px; padding: 4px 12px; line-height: 1.1; }
  .btn-benefits { background: var(--ink); color: var(--white); outline: 2px solid var(--brand-yellow); outline-offset: 2px; align-self: flex-start; }
  .btn-how { background: var(--white); color: var(--ink); }
  .btn-how em { display: block; font-family: "Playfair Display", serif; font-size: 13px; font-weight: 400; }

  .steps {
    position: absolute; top: 535px; left: 90px; right: 90px; height: 70px;
    display: flex; align-items: center; justify-content: space-between;
    border-top: 1px solid var(--line);
    padding-top: 18px;
  }
  .step { display: flex; align-items: center; gap: 10px; text-align: left; font-size: 11px; font-weight: 700; line-height: 1.25; width: 220px; }
  .step-icon { flex: none; width: 36px; height: 40px; border-radius: 6px; background: var(--teal); opacity: .85; }
  .know-more { font-family: "Playfair Display", serif; font-style: italic; font-size: 18px; text-align: center; }
  .know-more svg { display: block; margin: 2px auto 0; }
</style>
</head>
<body>
<div class="page">
  <header class="site-header">
    <div class="brand"><span class="brand-name">DINVORA</span><span class="brand-tag">BETA</span></div>
    <nav class="main-nav">
      <span class="active">HOME</span><span>BENEFITS</span><span>HOW IT WORKS</span><span>CONTACT</span>
    </nav>
    <div class="account-links">SIGN UP<span>/</span>SIGN IN</div>
  </header>

  <section class="hero" role="img" aria-label="Overhead photo of a rustic purple wooden table with a chopping board, mortar and pestle, herbs, spices, lemon and knives">
    <div class="hero-content">
      <h1 class="hero-title">CHEF MADE MEALS IN YOUR HOME</h1>
      <div class="cta-chef"><strong>BECOME A PRIVATE CHEF</strong><em>Earn extra money as a private chef.</em></div>
      <div class="secondary-actions">
        <span class="btn btn-benefits">CHEF BENEFITS</span>
        <span class="btn btn-how">HOW IT WORKS<em>for clients</em></span>
      </div>
      <div class="steps">
        <div class="step"><span class="step-icon" role="img" aria-label="Icon of a chef"></span>BOOK A<br>CHEF</div>
        <div class="step"><span class="step-icon" role="img" aria-label="Icon of a chef carrying ingredients"></span>THE CHEF WILL BRING ALL<br>NECESSARY INGREDIENTS<br>TO YOUR HOME</div>
        <div class="know-more">know more
          <svg width="18" height="10" viewBox="0 0 18 10"><path d="M2 2 L9 8 L16 2" fill="none" stroke="#e9c21b" stroke-width="2.5"/></svg>
        </div>
        <div class="step"><span class="step-icon" role="img" aria-label="Icon of a chef cooking"></span>THE CHEF WILL COOK<br>FOR YOU AND<br>YOUR GUESTS</div>
        <div class="step"><span class="step-icon" role="img" aria-label="Icon of guests dining at a table"></span>YOU CAN RELAX<br>AND ENJOY<br>THE PARTY</div>
      </div>
    </div>
  </section>
</div>
</body>
</html>
```